New Business Card Design Project VORALDI-Italy

we are VORALDI-Italy
our company in the market for 3 years we are luxury cosmetic company and its about time for a facelift :)
i will like to have elegant luxurious and unique business card
that will give the person that get it a unique, luxurious and elegant impression
I'm VERY OPEN FOR NEW IDEAS , even duo i add a few files of things that i see on line and i like them

i add my logo as well
my website is VORALDI.COM
(if you would like to see the main style that we have)

Target Market(s)

adult that have money :)

Industry/Entity Type

Business

Contact Information for Business Card

Name - Paul Voraldi
Position - CEO and CO Founder
address - 4718 E Danbury
telephone - 555-318-4402
email - paul@voraldi-example.com
fax - 555-318-4402
website - VORALDI.COM

Colors
000000
959595
fbee3e
ffffff

Requirements
Must have
• big logo in GOLD color
• elegant look
• impressive
Nice to have
• not must but maybe classy pattern background
• not must but maybe emblem
• maybe clear plastic business card
Should not have
• colors
• images

```html
<!DOCTYPE html>
<html lang="en">
<head>
<meta charset="utf-8">
<title>VORALDI Italy – Business Card</title>
<link rel="stylesheet" href="https://fonts.googleapis.com/css2?family=Cinzel:wght@400&family=Roboto:wght@400&display=swap">
<style>
  :root {
    --backdrop: #d9d3cb;
    --card-light: #2e2e2e;
    --card-dark: #0c0c0c;
    --gold: #c9a93a;
    --title-grey: #a9a9a9;
    --contact-grey: #c4c4c4;
  }
  html, body {
    margin: 0;
    padding: 0;
    overflow: hidden;
  }
  .canvas {
    position: relative;
    width: 1200px;
    height: 970px;
    background: var(--backdrop);
    overflow: hidden;
  }
  .card {
    position: absolute;
    left: 178px;
    top: 268px;
    width: 844px;
    height: 482px;
    border-radius: 18px;
    background: linear-gradient(100deg, var(--card-light) 0%, #1a1a1a 45%, var(--card-dark) 60%, #222 100%);
    overflow: hidden;
  }
  .holder-name {
    position: absolute;
    left: 50px;
    top: 68px;
    margin: 0;
    font-family: "Cinzel", serif;
    font-weight: 400;
    font-size: 34px;
    letter-spacing: 1px;
    color: var(--gold);
    line-height: 1;
  }
  .holder-role {
    position: absolute;
    left: 47px;
    top: 109px;
    margin: 0;
    font-family: "Roboto", sans-serif;
    font-size: 21px;
    color: var(--title-grey);
    line-height: 1;
  }
  .contact-list {
    position: absolute;
    left: 49px;
    top: 259px;
    margin: 0;
    padding: 0;
    list-style: none;
    font-family: "Roboto", sans-serif;
    font-size: 20px;
    line-height: 33.8px;
    color: var(--contact-grey);
  }
  .brand {
    position: absolute;
    left: 420px;
    top: 70px;
    width: 390px;
    text-align: center;
  }
  .brand-circle {
    display: block;
    margin: 0 auto;
  }
  .brand-name {
    margin: 40px 0 0;
    font-family: "Cinzel", serif;
    font-weight: 400;
    font-size: 70px;
    line-height: 1;
    color: var(--gold);
    letter-spacing: 1px;
  }
  .brand-rule {
    display: block;
    margin: 12px auto 0;
    width: 380px;
    height: 3px;
    background: var(--gold);
  }
  .brand-country {
    margin: 14px 0 0;
    font-family: "Cinzel", serif;
    font-weight: 400;
    font-size: 28px;
    line-height: 1;
    color: var(--gold);
    letter-spacing: 1px;
  }
</style>
</head>
<body>
<main class="canvas">
  <section class="card" aria-label="VORALDI Italy business card">
    <h1 class="holder-name">PAUL VORALDI</h1>
    <p class="holder-role">CEO and CO Founder</p>
    <ul class="contact-list">
      <li>Tel. 555-318-4402</li>
      <li>Fax. 555-318-4402</li>
      <li>paul@voraldi-example.com</li>
      <li>www.voraldi.com</li>
      <li>Address. 4718 E Danbury</li>
    </ul>
    <div class="brand">
      <svg class="brand-circle" width="176" height="176" viewBox="0 0 176 176" aria-hidden="true">
        <circle cx="88" cy="88" r="84" fill="none" stroke="var(--gold)" stroke-width="3"/>
      </svg>
      <p class="brand-name">VORALDI</p>
      <span class="brand-rule"></span>
      <p class="brand-country">ITALY</p>
    </div>
  </section>
</main>
</body>
</html>
```